National Networking/Telecommunications Company needs a new packaging (bag) design

We are currently going through a re-branding stage and need to create new packaging for all of our material.

We need a complete redesign of our current packaging (which is in various sizes). I have attached the current die-lines/knife for one of our bags.

- VORELTA logos to be changed to our PLANOVA logo (attached)
- PLANOVA logo to be modified, so it simply says the word PLANOVA with the tick image on the end. Please remove all other writing (GLOBAL SOLUTIONS & BOLD NAME, SUPERIOR WORTH) removed from the logo. Once this has been removed, please resize the word PLANOVA, so it fits nicely beside the tick logo.
- Please remove all references to VORELTA websites, and replace with www.planova.com.au
- Remove "Network, Computer and Audio Video Connectivity Solutions"
- Keeping the logos that say "Lifetime Warranty" and "100% Tested and Certified", open to different ideas on how to portray them on the bag.
- Our main company colours are red, blue & silver. We're open to all designs. Packaging needs to STAND OUT, without looking cheap. Needs to still look professional and classy.
- The inside backing of the bag is to be white in colour.

I have attached our new cable box design, if that helps with keeping the colours the same.

Target Market(s)

Electrical wholesalers (who stock this product), IT/System Integrators, Installers

Industry/Entity Type

Telecommunications

Font styles to use
Sans Serif

Requirements
Must have
• Our company colours (blue, red, white/silver)
Nice to have
• Overall design needs to be simplistic, yet elegant and professional.
Should not have
• Should not have the word VORELTA anywhere

```html
<!DOCTYPE html>
<html lang="en">
<head>
<meta charset="utf-8">
<title>Bag Packaging Concept</title>
<link rel="stylesheet" href="https://fonts.googleapis.com/css2?family=Exo+2:wght@600&family=Source+Sans+3:wght@400&display=swap">
<style>
  :root {
    --canvas: #ffffff;
    --dieline: #8fd3ea;
    --accent-cyan: #14a1d3;
    --navy: #1b3281;
    --white: #ffffff;
    --note-grey: #707070;
  }
  * { margin: 0; padding: 0; box-sizing: border-box; }
  html, body {
    width: 1200px;
    height: 880px;
    overflow: hidden;
    background: var(--canvas);
  }
  .artboard {
    position: relative;
    width: 1200px;
    height: 880px;
    background: var(--canvas);
  }

  /* Front of bag */
  .bag-front {
    position: absolute;
    left: 83px;
    top: 70px;
    width: 473px;
    height: 754px;
    border: 1px solid var(--dieline);
    background: var(--white);
  }
  .bag-front__seal {
    position: absolute;
    left: 0;
    top: 45px;
    width: 100%;
    height: 0;
    border-top: 1.5px solid var(--dieline);
  }
  .bag-front__hang-hole {
    position: absolute;
    left: 196px;
    top: 74px;
    width: 82px;
    height: 36px;
  }
  .bag-front__accent {
    position: absolute;
    left: 0;
    top: 0;
    width: 473px;
    height: 754px;
  }
  .bag-front__note {
    position: absolute;
    left: 32px;
    top: 456px;
    width: 420px;
    font-family: "Source Sans 3", sans-serif;
    font-size: 22.5px;
    line-height: 28px;
    color: var(--note-grey);
  }

  /* Back of bag */
  .bag-back {
    position: absolute;
    left: 669px;
    top: 70px;
    width: 483px;
    height: 748px;
    background: var(--navy);
  }
  .feature {
    position: absolute;
    display: flex;
    align-items: center;
  }
  .feature--warranty { top: 180px; left: 50px; }
  .feature--tested { top: 445px; left: 50px; }
  .feature__icon {
    flex: none;
    width: 116px;
    height: 116px;
  }
  .feature__badge {
    flex: none;
    width: 115px;
    height: 115px;
    border-radius: 50%;
    background: var(--white);
  }
  .feature__label {
    margin-left: 25px;
    font-family: "Exo 2", sans-serif;
    font-weight: 600;
    font-size: 40px;
    line-height: 44px;
    color: var(--white);
    letter-spacing: 0.3px;
  }
  .feature--tested .feature__label { margin-left: 21px; font-size: 40.5px; }
</style>
</head>
<body>
<main class="artboard">

  <section class="bag-front" aria-label="Bag front">
    <svg class="bag-front__accent" viewBox="0 0 473 754" aria-hidden="true">
      <polygon points="0,142 473,142 473,204 147,425 0,295" fill="var(--accent-cyan)"/>
    </svg>
    <div class="bag-front__seal"></div>
    <svg class="bag-front__hang-hole" viewBox="0 0 82 36" aria-hidden="true">
      <path d="M1,17 H25 A16,16 0 0 1 57,17 H81 V35 H1 Z" fill="none" stroke="var(--dieline)" stroke-width="1.5"/>
    </svg>
    <p class="bag-front__note">This shape inspired from the ‘Tick’ symbol, of the logo.</p>
  </section>

  <section class="bag-back" aria-label="Bag back">
    <div class="feature feature--warranty">
      <svg class="feature__icon" viewBox="0 0 116 116" aria-hidden="true">
        <g fill="none" stroke="var(--white)" stroke-width="6" stroke-linecap="round">
          <path d="M14,44 A46,46 0 0 1 94,24"/>
          <path d="M102,72 A46,46 0 0 1 22,92"/>
          <circle cx="58" cy="58" r="32"/>
          <path d="M58,36 V60 L48,75"/>
          <path d="M58,28 V33 M58,83 V88 M28,58 H33 M83,58 H88"/>
        </g>
        <polygon points="104,12 106,36 84,30" fill="var(--white)"/>
        <polygon points="12,104 10,80 32,86" fill="var(--white)"/>
      </svg>
      <p class="feature__label">Lifetime<br>Warranty</p>
    </div>

    <div class="feature feature--tested">
      <div class="feature__badge" role="img" aria-label="Testing certification badge"></div>
      <p class="feature__label">100% Tested<br>and Certified</p>
    </div>
  </section>

</main>
</body>
</html>
```